Looking to design a new sign for our church.

Looking for a new sign
4 x 8 feet dimension
We are renaming the church "Keller Ridge Community Church"
looking for legible graphics
Would like some type of backdrop being a family tree (oak) / open to other ideas as you are led
I have included a pic of the old sign for your review
would like to incorporate our ministry logo on the lower right hand corner of the sign / see file attached

```html
<!DOCTYPE html>
<html lang="en">
<head>
<meta charset="UTF-8">
<title>Keller Ridge Community Church – Sign</title>
<link rel="stylesheet" href="https://fonts.googleapis.com/css2?family=Oswald:wght@700&family=Montserrat:wght@600&display=swap">
<style>
  :root {
    --backdrop: #d6d6d6;
    --sign-face: #ffffff;
    --ink-green: #0f2a12;
    --canopy-deep: #132e15;
    --canopy-mid: #1f4622;
  }
  html, body {
    margin: 0;
    padding: 0;
    width: 928px;
    height: 1200px;
    overflow: hidden;
    background: var(--backdrop);
  }
  .canvas {
    position: relative;
    width: 928px;
    height: 1200px;
  }
  .sign {
    position: absolute;
    left: 24px;
    top: 380px;
    width: 880px;
    height: 440px;
    background: var(--sign-face);
    box-shadow: 6px 10px 22px rgba(0, 0, 0, 0.28);
    overflow: hidden;
  }
  .oak-backdrop {
    position: absolute;
    left: 0;
    top: 0;
    width: 382px;
    height: 440px;
  }
  .church-name {
    position: absolute;
    left: 409px;
    top: 172px;
    width: 430px;
    text-align: center;
    color: var(--ink-green);
  }
  .church-name__title {
    margin: 0;
    font-family: "Oswald", sans-serif;
    font-weight: 700;
    font-size: 58px;
    line-height: 1;
    letter-spacing: 0.01em;
    text-transform: uppercase;
  }
  .church-name__subtitle {
    margin: 8px 0 0;
    font-family: "Montserrat", sans-serif;
    font-weight: 600;
    font-size: 16px;
    letter-spacing: 0.34em;
    text-transform: uppercase;
  }
  .ministry-mark {
    position: absolute;
    right: 36px;
    bottom: 30px;
    display: flex;
    flex-direction: column;
    align-items: flex-end;
    gap: 8px;
    color: var(--ink-green);
  }
  .ministry-mark__dot {
    width: 42px;
    height: 42px;
    border-radius: 50%;
    background: var(--ink-green);
    margin-right: 18px;
  }
  .ministry-mark__name {
    font-family: "Montserrat", sans-serif;
    font-weight: 600;
    font-size: 10px;
    letter-spacing: 0.12em;
    text-transform: uppercase;
  }
</style>
</head>
<body>
  <div class="canvas">
    <section class="sign">
      <svg class="oak-backdrop" viewBox="0 0 382 440" role="img" aria-label="Dark green silhouette of a spreading oak tree with visible roots, the family tree backdrop">
        <defs>
          <radialGradient id="canopyTone" cx="45%" cy="42%" r="65%">
            <stop offset="0%" stop-color="var(--canopy-deep)"/>
            <stop offset="70%" stop-color="var(--canopy-mid)"/>
            <stop offset="100%" stop-color="var(--canopy-mid)" stop-opacity="0"/>
          </radialGradient>
        </defs>
        <rect width="382" height="440" fill="url(#canopyTone)"/>
      </svg>

      <div class="church-name">
        <h1 class="church-name__title">Keller Ridge</h1>
        <p class="church-name__subtitle">Community Church</p>
      </div>

      <div class="ministry-mark">
        <div class="ministry-mark__dot"></div>
        <span class="ministry-mark__name">Open Field Missions</span>
      </div>
    </section>
  </div>
</body>
</html>
```